What does your organisation do?
TALVIN
We need a website for our business – A Holding Company

Objective:
1. User-friendly design and navigation
2. Content management
3. Language (English and Arabic)
4. Download PDF or scan for profile

Navigations and Sub-Navigations:
1. Profile
a. About Us
b. Vision-Mission
c. Corporate Governance
d. Sustainability
2. Business Sector
a. Food
b. Logistics
c. Retail
d. Trading and Distribution
e. Government Services
3. Investor Relations
4. Careers
5. Contact Us
Footer:
Contact Us
1. Address
2. Contact Number
3. Email Address
4. Social Media (LinkedIn Logo)
Company / Quick Links
• About Us
• Vision & Mission
• Careers

Newsletter
Get the latest information from us and our group companies. Be amongst the first to know and stay updated on the go. Join our mailing list
Email Text Box with Subscribe button.

Competitors / Reference:
URL 1: https://www.qorimbeholding.example/
URL 2: https://www.veluntaholding.example/
URL 3: https://pmx.example

Target Market(s)

Individual and customer businesses customers

Industry/Entity Type

Financial

Coding

Coded - Design and coding required

Number of Pages Required

5+ page

Font styles to use
Serif
Sans Serif

Requirements
Must have

• 1. SEO Friendly website ( Meta tags, description, title, proper keywords)
2. Ability to make modifications easily in future. (Provide front end for adding content, images etc.)
3. Chatbot Widget with enquiry form – integration with google sheet
4. Register website with Google (Google Search Console)
5. Register website with Google My Business
Nice to have
• See uploaded file for reference

```html
<!DOCTYPE html>
<html lang="en">
<head>
<meta charset="utf-8">
<title>TALVIN Holding Company</title>
<meta name="description" content="TALVIN is a diversified holding company with businesses in food, logistics, retail, trading and distribution, and government services.">
<meta name="keywords" content="holding company, investments, food, logistics, retail, trading, distribution, government services">
<link href="https://fonts.googleapis.com/css2?family=Montserrat:wght@400;500;600;700;800&display=swap" rel="stylesheet">
<style>
:root{
  --red:#f4443a;
  --ink:#1d1d1f;
  --text:#555559;
  --line:#e4e4e6;
  --dark:#222226;
  --card-dark:#1a1a1d;
  --white:#ffffff;
}
*{margin:0;padding:0;box-sizing:border-box}
html,body{width:1200px;height:4127px;overflow:hidden}
body{position:relative;font-family:"Montserrat",sans-serif;color:var(--text);background:var(--white)}
section,header,footer{position:absolute;left:0;width:1200px}
.btn{position:absolute;display:flex;align-items:center;justify-content:center;background:var(--red);color:var(--white);font-weight:600;font-size:15px;letter-spacing:.5px;border-radius:3px;text-decoration:none}

/* header */
.site-header{top:0;height:70px;background:var(--white)}
.brand{position:absolute;display:flex;align-items:center;gap:10px;font-weight:500;letter-spacing:1px}
.brand-mark{width:20px;height:20px;border:2.5px solid var(--red)}
.site-header .brand{left:58px;top:18px;font-size:28px;color:var(--ink)}
.main-nav{position:absolute;right:230px;top:28px;display:flex;gap:22px;font-size:12px;color:var(--ink);white-space:nowrap}
.main-nav .active{color:var(--red);position:relative}
.main-nav .active::before{content:"";position:absolute;left:-12px;top:5px;width:5px;height:5px;border-radius:50%;background:var(--red)}
.site-header .btn{left:1004px;top:16px;width:134px;height:40px}

/* hero */
.hero{top:70px;height:642px;background:linear-gradient(100deg,#5b5a56 0%,#8d8274 35%,#c7955a 60%,#6d5a48 85%,#3e3a36 100%)}
.hero-title{position:absolute;left:0;width:1200px;top:188px;text-align:center;color:var(--white);font-weight:800;font-size:60px;line-height:64px;letter-spacing:1px}
.hero-sub{position:absolute;left:0;width:1200px;top:336px;text-align:center;color:var(--white);font-size:15px;line-height:24px}
.hero .btn{left:532px;top:400px;width:134px;height:38px}
.slider-line{position:absolute;left:972px;top:597px;width:48px;height:2px;background:var(--red)}
.slider-dot{position:absolute;top:579px;width:36px;height:36px;border-radius:50%;border:2px solid var(--white);display:flex;align-items:center;justify-content:center}
.slider-dot.prev{left:1031px;border-color:var(--red)}
.slider-dot.next{left:1076px}

/* welcome */
.welcome{top:712px;height:338px;background:var(--red);color:var(--white);text-align:center}
.welcome .eyebrow{position:absolute;left:0;width:1200px;top:74px;font-size:16px}
.welcome h1{position:absolute;left:0;width:1200px;top:98px;font-size:31px;font-weight:600}
.welcome p{position:absolute;left:330px;width:540px;font-size:11.5px;line-height:21px}
.scroll-down{position:absolute;left:574px;top:1024px;width:52px;height:52px;border-radius:50%;background:var(--white);display:flex;align-items:center;justify-content:center;z-index:2}
.scroll-down span{width:44px;height:44px;border-radius:50%;background:var(--ink);display:flex;align-items:center;justify-content:center}

/* sectors */
.sectors{top:1050px;height:706px}
.section-title{font-weight:500;color:var(--ink);font-size:30px}
.sectors .section-title{position:absolute;left:143px;top:76px}
.sectors .intro{position:absolute;left:599px;top:90px;width:380px;font-size:11.5px;line-height:21px}
.sector-card{position:absolute;top:187px;width:284px;height:443px;border:1px solid var(--line);text-align:center}
.sector-card .media{height:225px}
.sector-card h3{margin-top:34px;font-size:16px;font-weight:600;color:var(--ink)}
.sector-card p{margin:14px auto 0;width:240px;font-size:11px;line-height:21px}

/* newsletter banner */
.newsletter{top:1756px;height:322px;background:linear-gradient(90deg,#b4bcc6 0%,#cfd5dc 40%,#d9c9b9 70%,#c8ccd3 100%)}
.newsletter h2{position:absolute;left:193px;top:68px;font-size:33px;font-weight:500;line-height:39px;color:var(--ink)}
.newsletter p{position:absolute;left:193px;top:157px;width:520px;font-size:11.5px;line-height:21px;color:#444}
.newsletter .btn{left:193px;top:214px;width:135px;height:38px}

/* more sectors */
.special{top:2078px;height:540px}
.special .section-title{position:absolute;left:0;width:1200px;top:68px;text-align:center;font-size:31px}
.special-card{position:absolute;top:192px;width:276px;height:270px;border:1px solid var(--line);text-align:center}
.special-icon{position:absolute;top:154px;width:82px;height:82px;background:var(--red);display:flex;align-items:center;justify-content:center;z-index:2}
.special-card h3{margin-top:60px;font-size:16px;font-weight:600;color:var(--ink)}
.special-card p{margin:18px auto 0;width:236px;font-size:11px;line-height:19.5px}
.special-card a{display:inline-block;margin-top:14px;font-size:13px;font-weight:600;color:var(--red);text-decoration:underline}

/* testimonials */
.testimonials{top:2618px;height:409px;background:var(--dark);overflow:hidden}
.t-arrows{position:absolute;left:60px;top:224px;display:flex;gap:12px}
.t-card{position:absolute;top:76px;width:455px;height:176px;background:var(--card-dark);border-left:3px solid var(--red);padding:64px 36px 0 28px;color:#c9c9cc;font-size:11.5px;line-height:21px}
.t-card::after{content:"";position:absolute;left:52px;bottom:-22px;border-left:22px solid transparent;border-top:22px solid var(--card-dark)}
.t-author{position:absolute;top:270px;display:flex;align-items:center;gap:14px}
.avatar{width:56px;height:56px;border-radius:50%;background:linear-gradient(135deg,#d9c2a8,#8d6e57)}
.t-author b{display:block;color:var(--red);font-size:12.5px;font-weight:500}
.t-author small{display:block;color:#9a9a9e;font-size:11px}

/* group companies */
.clients{top:3027px;height:261px;background:var(--red)}
.clients .section-title{position:absolute;left:0;width:1200px;top:70px;text-align:center;color:var(--white);font-size:33px}
.client-row{position:absolute;left:170px;top:152px;width:860px;display:flex;justify-content:space-between;align-items:center}
.client-name{display:flex;align-items:center;gap:8px;color:var(--white);font-weight:700;font-size:21px;letter-spacing:1px}
.client-name i{width:14px;height:14px;background:var(--white);display:block}
.c-arrow{position:absolute;top:160px}

/* faq */
.faq{top:3288px;height:537px}
.faq .section-title{position:absolute;left:0;width:1200px;top:73px;text-align:center;font-size:30px}
.faq-item{position:absolute;left:281px;width:637px;height:42px;border:1px solid var(--line);border-radius:3px;display:flex;align-items:center;padding:0 20px 0 12px;font-size:12px;color:var(--ink)}
.faq-item .q{width:25px;height:25px;border-radius:50%;background:var(--ink);color:var(--white);font-size:13px;font-weight:700;display:flex;align-items:center;justify-content:center;margin-right:32px}
.faq-item .toggle{margin-left:auto;font-size:20px;color:var(--ink)}
.faq-item.open{border-color:var(--red);color:var(--red);height:46px}
.faq-item.open .q{background:var(--red)}
.faq-item.open .toggle{color:var(--red)}
.faq-answer{position:absolute;left:281px;top:200px;width:637px;height:97px;border:1px solid var(--line);border-radius:3px;padding:26px 60px 0 58px;font-size:11px;line-height:20px}

/* footer */
.site-footer{top:3825px;height:302px;background:var(--dark);color:#d2d2d5}
.f-col{position:absolute;top:48px}
.f-col h4{color:var(--white);font-size:14.5px;font-weight:500;margin-bottom:24px}
.f-col ul{list-style:none;font-size:11.5px;line-height:22.5px}
.f-col li{position:relative;padding-left:19px}
.f-col li::before{content:"";position:absolute;left:0;top:9px;width:5px;height:5px;border-radius:50%;background:var(--red)}
.contact-row{display:flex;gap:14px;font-size:11.5px;line-height:20px;margin-bottom:14px}
.contact-row svg{flex:none;margin-top:3px}
.site-footer .brand{left:893px;top:108px;font-size:28px;color:var(--white)}
.socials{position:absolute;left:912px;top:158px;display:flex;gap:5px}
.socials span{width:32px;height:32px;border-radius:50%;border:1.5px solid var(--red)}
.f-divider{position:absolute;left:0;top:262px;width:1200px;height:1px;background:#343438}
.copyright{position:absolute;left:0;width:1200px;top:276px;text-align:center;font-size:11px}
.copyright b{color:var(--red);font-weight:400}
</style>
</head>
<body>

<header class="site-header">
  <div class="brand"><span class="brand-mark"></span>TALVIN</div>
  <nav class="main-nav">
    <span class="active">Profile</span><span>Business Sector</span><span>Investor Relations</span><span>Careers</span><span>Contact Us</span>
  </nav>
  <a class="btn">ENQUIRE</a>
</header>

<section class="hero" role="img" aria-label="City skyline and highway at sunset">
  <h2 class="hero-title">INVESTING IN<br>TOMORROW</h2>
  <p class="hero-sub">TALVIN Is A Diversified Holding Company Building Growth,<br>Value And Trust Across The Region.</p>
  <a class="btn">OUR PROFILE</a>
  <span class="slider-line"></span>
  <span class="slider-dot prev"><svg width="10" height="14" viewBox="0 0 10 14"><path d="M8 1 2 7l6 6" fill="none" stroke="#f4443a" stroke-width="2"/></svg></span>
  <span class="slider-dot next"><svg width="10" height="14" viewBox="0 0 10 14"><path d="m2 1 6 6-6 6" fill="none" stroke="#fff" stroke-width="2"/></svg></span>
</section>

<section class="welcome">
  <p class="eyebrow">Welcome To</p>
  <h1>TALVIN Holding Company</h1>
  <p style="top:150px">TALVIN brings together a group of businesses serving individuals and companies across the UAE. Guided by clear values and sound corporate governance, we invest for long term, sustainable growth.</p>
  <p style="top:226px">Our vision is to create lasting value for investors, partners and communities on every step of the journey.</p>
</section>
<div class="scroll-down"><span><svg width="20" height="18" viewBox="0 0 20 18"><path d="m3 2 7 6 7-6M3 9l7 6 7-6" fill="none" stroke="#fff" stroke-width="2"/></svg></span></div>

<section class="sectors">
  <h2 class="section-title">Our Business Sectors</h2>
  <p class="intro">A Balanced Portfolio Of Businesses Serving Individual And Corporate Customers Across The Region.</p>
  <article class="sector-card" style="left:143px">
    <div class="media" role="img" aria-label="Fresh food products" style="background:linear-gradient(135deg,#3e5478,#9aa3b0 60%,#d6b58c)"></div>
    <h3>Food</h3>
    <p>Our food businesses source, produce and supply quality products to homes, restaurants and retailers, with a strong focus on safety, freshness and reliable service across the UAE.</p>
  </article>
  <article class="sector-card" style="left:458px">
    <div class="media" role="img" aria-label="Logistics network with ship, plane and truck" style="background:linear-gradient(135deg,#1d6fc4,#2f8ee0 55%,#3fb5a8)"></div>
    <h3>Logistics</h3>
    <p>Our land, sea and air network moves goods for businesses and individuals, with warehousing, freight and last mile delivery backed by modern tracking technology.</p>
  </article>
  <article class="sector-card" style="left:773px">
    <div class="media" role="img" aria-label="Retail store and online shopping" style="background:linear-gradient(180deg,#2d5a8c,#5d86b5 70%,#dfe4ea)"></div>
    <h3>Retail</h3>
    <p>Our retail brands serve customers in store and online, offering well chosen products, fair prices and a friendly, consistent shopping experience.</p>
  </article>
</section>

<section class="newsletter" role="img" aria-label="Team at work in an office">
  <h2>Stay Ahead With Our<br>Group News &amp; Updates</h2>
  <p>Get the latest information from us and our group companies. Be amongst the first to know and stay updated on the go. Join our mailing list.</p>
  <a class="btn">SUBSCRIBE</a>
</section>

<section class="special">
  <h2 class="section-title">More Sectors</h2>
  <div class="special-icon" style="left:409px"><svg width="44" height="44" viewBox="0 0 44 44" fill="none" stroke="#fff" stroke-width="1.6"><rect x="5" y="16" width="16" height="14"/><rect x="23" y="16" width="16" height="14"/><path d="M13 16V10h18v6M5 34h34"/></svg></div>
  <article class="special-card" style="left:312px">
    <h3>Trading And Distribution</h3>
    <p>We import, trade and distribute a wide range of goods, linking trusted international suppliers with local markets through an efficient and dependable supply chain.</p>
    <a>More</a>
  </article>
  <div class="special-icon" style="left:708px"><svg width="44" height="44" viewBox="0 0 44 44" fill="none" stroke="#fff" stroke-width="1.6"><path d="M6 16 22 7l16 9H6zM6 36h32M10 18v15M18 18v15M26 18v15M34 18v15"/></svg></div>
  <article class="special-card" style="left:611px">
    <h3>Government Services</h3>
    <p>TALVIN helps companies get up and running quickly by handling the time-consuming procedures for visas, permits and licenses.</p>
    <a>More</a>
  </article>
</section>

<section class="testimonials">
  <div class="t-arrows">
    <svg width="30" height="14" viewBox="0 0 30 14"><path d="M29 7H2m6-6L2 7l6 6" fill="none" stroke="#fff" stroke-width="2"/></svg>
    <svg width="30" height="14" viewBox="0 0 30 14"><path d="M1 7h27m-6-6 6 6-6 6" fill="none" stroke="#f4443a" stroke-width="2"/></svg>
  </div>
  <blockquote class="t-card" style="left:165px">Lorem Ipsum has been the industry's standard dummy text ever since the 1500s, when an this unknown printer took a galley of type scrambled it to make a type specimen book. It has survived not only five centuries, but also the leap into electronic typesetting, remaining...</blockquote>
  <div class="t-author" style="left:232px"><span class="avatar" role="img" aria-label="Client portrait"></span><div><b>Client Name</b><small>something.com</small></div></div>
  <blockquote class="t-card" style="left:660px">Lorem Ipsum has been the industry's standard dummy text ever since the 1500s, when an this unknown printer took a galley of type scrambled it to make a type specimen book. It has survived not only five centuries, but also the leap into electronic typesetting, remaining...</blockquote>
  <div class="t-author" style="left:733px"><span class="avatar" role="img" aria-label="Client portrait"></span><div><b>Client Name</b><small>something.com</small></div></div>
  <blockquote class="t-card" style="left:1155px">Lorem Ipsum has been the industry's standard dummy text ever since the 1500s, when an this unknown printer took a galley of type scrambled it to make a type specimen book.</blockquote>
</section>

<section class="clients">
  <h2 class="section-title">Our Group Companies</h2>
  <svg class="c-arrow" style="left:122px" width="16" height="28" viewBox="0 0 16 28"><path d="M14 2 2 14l12 12" fill="none" stroke="#fff" stroke-width="2"/></svg>
  <div class="client-row">
    <span class="client-name"><i></i>KESTREL</span>
    <span class="client-name"><i></i>ARDENA</span>
    <span class="client-name"><i></i>KESTREL</span>
    <span class="client-name"><i></i>ARDENA</span>
    <span class="client-name"><i></i>KESTREL</span>
  </div>
  <svg class="c-arrow" style="left:1054px" width="16" height="28" viewBox="0 0 16 28"><path d="m2 2 12 12L2 26" fill="none" stroke="#fff" stroke-width="2"/></svg>
</section>

<section class="faq">
  <h2 class="section-title">Faq's</h2>
  <div class="faq-item open" style="top:147px"><span class="q">?</span>Lorem Ipsum Is Simply Text of the Printing And type ?<span class="toggle">&minus;</span></div>
  <div class="faq-answer">It has survived not only five centuries, but also the leap into electronic typesetting, remaining essentially unchanged. It was popularised in the 1960s with the release of Letraset sheets containing more recently with desktop.</div>
  <div class="faq-item" style="top:310px"><span class="q">?</span>Lorem Ipsum Is Simply Text of the Printing And type ?<span class="toggle">+</span></div>
  <div class="faq-item" style="top:364px"><span class="q">?</span>Lorem Ipsum Is Simply Text indutry of the Printing And type indutsry ?<span class="toggle">+</span></div>
  <div class="faq-item" style="top:418px"><span class="q">?</span>Lorem Ipsum Is Simply Text of the Printing And type ?<span class="toggle">+</span></div>
</section>

<footer class="site-footer">
  <div class="f-col" style="left:62px">
    <h4>Company</h4>
    <ul><li>About Us</li><li>Vision &amp; Mission</li><li>Investor Relations</li><li>Careers</li><li>Contact Us</li></ul>
  </div>
  <div class="f-col" style="left:337px">
    <h4>Business Sector</h4>
    <ul><li>Food</li><li>Logistics</li><li>Retail</li><li>Trading and Distribution</li><li>Government Services</li></ul>
  </div>
  <div class="f-col" style="left:613px;width:240px">
    <h4>Contact Us</h4>
    <div class="contact-row"><svg width="16" height="18" viewBox="0 0 16 18"><path d="M8 17s6-6 6-10A6 6 0 0 0 2 7c0 4 6 10 6 10z" fill="none" stroke="#f4443a" stroke-width="1.6"/><circle cx="8" cy="7" r="2" fill="#f4443a"/></svg><div><b style="color:var(--red);font-weight:400">Talvin</b><br>101 - Lorem ipsum simpl text print type setting text industry.</div></div>
    <div class="contact-row"><svg width="16" height="16" viewBox="0 0 16 16"><path d="M3 1h3l1.5 4-2 1.2a9 9 0 0 0 4.3 4.3L11 8.5l4 1.5v3a2 2 0 0 1-2 2A12 12 0 0 1 1 3a2 2 0 0 1 2-2z" fill="#f4443a"/></svg><div>123 456 7890</div></div>
    <div class="contact-row"><svg width="16" height="14" viewBox="0 0 16 14"><rect x="0" y="1" width="16" height="12" rx="1" fill="#f4443a"/><path d="m1 2 7 6 7-6" fill="none" stroke="#222226" stroke-width="1.4"/></svg><div>info@talvin.com</div></div>
  </div>
  <div class="brand"><span class="brand-mark"></span>TALVIN</div>
  <div class="socials" aria-label="Social media links"><span></span><span></span><span></span><span></span></div>
  <div class="f-divider"></div>
  <p class="copyright">©<b>Talvin Holding Company</b> -2021 All rights reserved.</p>
</footer>

</body>
</html>
```